Need corporate powerpoint template design for our sales proposals

Need corporate power point design template for our sales proposals. This powerpoint will be targeted at our customers when we are putting design proposals and pricing quotes together for them

Target Market(s)

Our customers

Industry/Entity Type

Sales

Requirements
Must have
• FernRidge name and logo somewhere
• Would like to have a cover slide and then non-cover slide as well as an ending slide for powerpoint templates
• Must have our corporate address and contact info somewhere, they are: FernRidge, Inc PO Box 47162 Oakland, California 94687. Office # 510-382-7419, email is info@fernridgeco.example
• I also attached an example business card to give you a sense of our design, also our website is www.fernridgeco.example
• Would like to match existing color scheme

```html
<!DOCTYPE html>
<html lang="en">
<head>
<meta charset="utf-8">
<title>FernRidge Presentation Template</title>
<link rel="stylesheet" href="https://fonts.googleapis.com/css2?family=EB+Garamond:wght@400;700&family=Carlito:wght@400;700&display=swap">
<style>
  :root {
    --stage: #bdbdc1;
    --paper: #ffffff;
    --green: #7cae44;
    --green-soft: #eef3e6;
    --green-veil: #8dbb5a;
    --ink: #4a4a4a;
    --ink-soft: #5a5a5a;
    --serif: "EB Garamond", Georgia, serif;
    --sans: "Carlito", "Calibri", Arial, sans-serif;
  }
  * { box-sizing: border-box; margin: 0; padding: 0; }
  html, body { width: 1200px; height: 1200px; overflow: hidden; background: var(--stage); }
  .board { position: relative; width: 1200px; height: 1200px; }
  .slide { position: absolute; width: 518px; height: 291px; background: var(--paper); overflow: hidden; }
  .slide--cover { left: 65px; top: 275px; }
  .slide--content { left: 618px; top: 275px; }
  .slide--cover-green { left: 65px; top: 634px; background: var(--green); }
  .slide--closing { left: 618px; top: 634px; }

  .decor { position: absolute; }
  .decor--cover { left: 0; top: 0; width: 240px; height: 200px;
    background: radial-gradient(ellipse at 30% 35%, var(--green-soft) 55%, rgba(238,243,230,0) 72%); }
  .decor--content { right: 0; top: 90px; width: 170px; height: 201px;
    background: radial-gradient(ellipse at 75% 60%, var(--green-soft) 50%, rgba(238,243,230,0) 72%); }
  .decor--green { left: 0; top: 0; width: 240px; height: 200px;
    background: radial-gradient(ellipse at 30% 35%, var(--green-veil) 55%, rgba(141,187,90,0) 72%); }
  .decor--closing { left: 0; top: 0; width: 240px; height: 150px;
    background: radial-gradient(ellipse at 30% 25%, var(--green) 55%, rgba(124,174,68,0) 75%); }

  .cover-title { position: absolute; left: 215px; top: 118px; font: 700 24px/1 var(--serif); color: var(--green); white-space: nowrap; }
  .cover-subtitle { position: absolute; left: 216px; top: 149px; font: 400 17.5px/1 var(--sans); color: var(--ink); }
  .slide--cover-green .cover-title { color: var(--paper); }
  .slide--cover-green .cover-subtitle { color: var(--ink-soft); }

  .brand { font: 400 19px/1 var(--serif); white-space: nowrap; display: inline-flex; align-items: center; gap: 4px; }
  .brand-dot { width: 6px; height: 6px; border-radius: 50%; background: currentColor; }
  .band { position: absolute; height: 19px; background: var(--green); }
  .slide--cover .band--stub { left: 0; top: 253px; width: 19px; }
  .slide--cover .band--long { left: 98px; right: 0; top: 253px; }
  .slide--cover .brand { position: absolute; left: 23px; top: 253px; color: var(--green); }
  .slide--cover-green .brand { position: absolute; left: 24px; top: 252px; color: var(--paper); }

  .content-title { position: absolute; left: 20px; top: 14px; font: 700 12px/1 var(--serif); color: var(--green); }
  .rule { position: absolute; height: 1px; background: var(--green); }
  .rule--top { left: 0; top: 38px; width: 470px; }
  .rule--bottom { left: 0; right: 14px; top: 272px; }
  .end-dot { position: absolute; right: 8px; top: 269px; width: 7px; height: 7px; border-radius: 50%; background: var(--green); }
  .slide--content .brand { position: absolute; right: 10px; top: 28px; font-size: 12px; color: var(--green); }
  .column { position: absolute; top: 52px; width: 186px; font-family: var(--sans); color: var(--ink); }
  .column--left { left: 20px; }
  .column--right { left: 264px; width: 180px; }
  .column h2 { font: 700 6.6px/1 var(--sans); color: var(--green); margin-bottom: 6px; }
  .column p { font-size: 5.4px; line-height: 8.8px; margin-bottom: 12px; }
  .column ul { list-style: none; }
  .column li { position: relative; padding-left: 13px; font-size: 5.4px; line-height: 8.8px; margin-bottom: 5.5px; }
  .column li::before { content: "•"; position: absolute; left: 0; color: var(--green); }

  .closing-title { position: absolute; left: 0; right: 0; top: 152px; text-align: center; font: 700 42px/1 var(--serif); color: var(--green); }
  .slide--closing .band--left { left: 0; width: 219px; top: 225px; }
  .slide--closing .band--right { left: 303px; right: 0; top: 225px; }
  .slide--closing .brand { position: absolute; left: 222px; top: 224px; color: var(--green); }
  .contact { position: absolute; left: 0; right: 0; top: 253px; text-align: center; font: 400 6px/9.5px var(--serif); color: var(--ink); }
</style>
</head>
<body>
<main class="board">

  <section class="slide slide--cover">
    <div class="decor decor--cover" role="img" aria-label="Large faint green leaf decoration"></div>
    <h1 class="cover-title">Your Title Goes Here</h1>
    <p class="cover-subtitle">Subtitle Goes Here</p>
    <div class="band band--stub"></div>
    <div class="band band--long"></div>
    <span class="brand">FernRidge</span>
  </section>

  <section class="slide slide--content">
    <div class="decor decor--content" role="img" aria-label="Faint green leaf decoration"></div>
    <h1 class="content-title">Title</h1>
    <div class="rule rule--top"></div>
    <span class="brand">FernRidge</span>
    <div class="column column--left">
      <h2>Heading 1</h2>
      <p>It is a long established fact that a reader will be distracted by the readable content of a page when looking at its layout. The point of using Lorem Ipsum is that it has a more-or-less normal distribution of letters, as opposed to using 'Content here, content here', making it look like readable English. Many desktop publishing packages and web page editors now use Lorem Ipsum as their default model text, and a search for 'lorem ipsum' will uncover many web sites still in their infancy. Various versions have evolved over the years, sometimes by accident, sometimes on purpose (injected humour and the like).</p>
      <h2>Heading 2</h2>
      <p>It is a long established fact that a reader will be distracted by the readable content of a page when looking at its layout. The point of using Lorem Ipsum is that it has a more-or-less normal distribution of letters, as opposed to using 'Content here, content here', making it look like readable English. Many desktop publishing packages and web page editors now use Lorem Ipsum as their default model text, and a search for 'lorem ipsum' will uncover many web sites still in their infancy. Various versions have evolved over the years, sometimes by accident, sometimes on purpose (injected humour and the like).</p>
    </div>
    <div class="column column--right">
      <h2>Heading 3</h2>
      <ul>
        <li>It is a long established fact that a reader will be distracted by the readable content of a page</li>
        <li>When looking at its layout. The point of using Lorem Ipsum is that it has a more-or-less normal distribution of letters</li>
        <li>As opposed to using 'Content here, content here', making it look like readable English.</li>
        <li>Many desktop publishing packages and web page editors now use Lorem Ipsum as their default model text.humour and the like).</li>
      </ul>
    </div>
    <div class="rule rule--bottom"></div>
    <div class="end-dot"></div>
  </section>

  <section class="slide slide--cover-green">
    <div class="decor decor--green" role="img" aria-label="Large tonal green leaf decoration"></div>
    <h1 class="cover-title">Your Title Goes Here</h1>
    <p class="cover-subtitle">Subtitle Goes Here</p>
    <span class="brand">FernRidge</span>
  </section>

  <section class="slide slide--closing">
    <div class="decor decor--closing" role="img" aria-label="Large green leaf decoration"></div>
    <h1 class="closing-title">Thanks and Q&amp;A</h1>
    <div class="band band--left"></div>
    <span class="brand">FernRidge</span>
    <div class="band band--right"></div>
    <p class="contact">FernRidge, Inc • PO Box 47162 Oakland • California 94687<br>Office: 510-382-7419 | Email: info@fernridgeco.example</p>
  </section>

</main>
</body>
</html>
```